Kelvaro Icon Contest

Kelvaro is a payment app that will allow tenants to pay their landlords and earn rewards. You can think of it link Pluxa for landlords and tenants. We want a sleek, modern design for the icons. The main colors are green, white, and black. You can get more inspiration from the website: https://kelvaro-pay.example/

For this contest, please design two icons. The first will be used to notify users that they have earned rewards (I.e. money). We are hoping for something more original than the traditional dollar sign or bag of money, but still easily recognizable as money. The second icon will show that a recurring rent payment has been established, successfully sent, or successfully received. This will be used for both tenants and landlords.

```html
<!DOCTYPE html>
<html lang="en">
<head>
<meta charset="utf-8">
<title>Kelvaro – Payment Successful Icon</title>
<link rel="stylesheet" href="https://fonts.googleapis.com/css2?family=Outfit:wght@700&display=swap">
<style>
  :root {
    --brand-green: #02663a;
    --icon-stroke: #ffffff;
    --page-bg: #ffffff;
  }
  * { margin: 0; padding: 0; box-sizing: border-box; }
  html, body {
    width: 1200px;
    height: 1200px;
    overflow: hidden;
    background: var(--page-bg);
  }
  .canvas {
    width: 1200px;
    height: 1200px;
    display: flex;
    flex-direction: column;
    align-items: center;
    justify-content: center;
  }
  .status-icon {
    width: 400px;
    height: 400px;
    display: block;
  }
  .status-label {
    margin-top: 34px;
    font-family: "Outfit", sans-serif;
    font-weight: 700;
    font-size: 86px;
    line-height: 87px;
    color: var(--brand-green);
    text-align: center;
    letter-spacing: 0.5px;
  }
</style>
</head>
<body>
  <main class="canvas">
    <svg class="status-icon" viewBox="0 0 304 304" role="img" aria-label="Payment sent arrow icon">
      <circle class="status-icon__disc" cx="152" cy="152" r="152" fill="var(--brand-green)"/>
      <path class="status-icon__arrow"
            d="M177 79 L257 148 L182 221 L179 173 C120 175 80 197 55 232 C65 180 105 130 174 124 Z"
            fill="none" stroke="var(--icon-stroke)" stroke-width="7" stroke-linejoin="round" stroke-linecap="round"/>
    </svg>
    <h1 class="status-label">Payment<br>Successful!</h1>
  </main>
</body>
</html>
```